Copper Ridge Resort & Marina - Boat Slips, Cabin Rentals, Floating Vacation Homes, & More

We need an 8'H x 16'W billboard for our Resort & marina, www.copperridgeresort.example. We'd like it to include: Lakefront Cabin Rentals, Floating Vacation Homes, and New Slips Summer 2022. We'd like it to be simple using the colors on our logo, similar to our business cards, and have our logo on it large. Maybe an arrow on the bottom pointing left that says 3 miles, possibly our website and phone number.

Target Market(s)

Lake People, Boaters

Industry/Entity Type

Resort & Marina (Recreation/Hospitality)

Font styles to use
Sans Serif
Other font styles liked:
• Simple/modern

Colors
0054AA
0677BA
7BADD7
CADEEF
E8F1F8
FFC000
F8CF3A
FAE287
FDF2CF
FEFAEE
F0912C
F2A743
F7CA91
FBE8D2
FDF5EE

Requirements
Must have
• Logo, Cabin Rentals, Floating Vacation Homes, New Slips Summer 2022
Nice to have
• An additional banner hanging from the bottom with an orange (or blue, colors from our logo) arrow pointing left, with white text saying: 3 miles 555-214-0867 www.copperridgeresort.example
Should not have
• Shouldn't be too busy

```html
<!DOCTYPE html>
<html lang="en">
<head>
<meta charset="utf-8">
<title>Copper Ridge Resort &amp; Marina – Billboard</title>
<link href="https://fonts.googleapis.com/css2?family=Tinos:wght@400;700&display=swap" rel="stylesheet">
<style>
  :root {
    --page: #ffffff;
    --board: #e1e4ed;
    --navy: #134b82;
    --coral: #e8553a;
    --amber: #f2a33a;
    --lake: #c3c7de;
    --white: #ffffff;
  }
  html, body {
    margin: 0;
    padding: 0;
    width: 1200px;
    height: 1200px;
    overflow: hidden;
    background: var(--page);
  }
  .canvas {
    position: relative;
    width: 1200px;
    height: 1200px;
  }
  .billboard {
    position: absolute;
    left: 73px;
    top: 313px;
    width: 1063px;
    height: 530px;
    background: var(--board);
    outline: 1px solid #555;
    overflow: hidden;
    font-family: "Tinos", "Times New Roman", serif;
  }
  .lake-map {
    position: absolute;
    left: 575px;
    top: 8px;
    width: 450px;
    height: 400px;
    border-radius: 45% 40% 35% 50%;
    background: radial-gradient(ellipse at 60% 45%, rgba(195,199,222,0.85) 0%, rgba(195,199,222,0.35) 55%, rgba(195,199,222,0) 75%);
  }
  .brand {
    position: absolute;
    left: 30px;
    top: 40px;
    width: 560px;
    text-align: center;
    color: var(--navy);
  }
  .brand-mark {
    display: block;
    width: 80px;
    height: 80px;
    margin: 0 auto 14px;
    border-radius: 50%;
    background: var(--amber);
  }
  .brand-name {
    margin: 0;
    font-weight: 400;
    font-size: 60px;
    line-height: 1;
    letter-spacing: 1px;
  }
  .brand-sub {
    display: block;
    margin-top: 12px;
    font-size: 26px;
    letter-spacing: 10px;
  }
  .directions {
    position: absolute;
    left: 97px;
    top: 285px;
    display: flex;
    align-items: center;
    gap: 22px;
  }
  .directions svg { display: block; }
  .distance {
    font-weight: 700;
    font-size: 90px;
    color: var(--coral);
    letter-spacing: -2px;
  }
  .contact {
    position: absolute;
    left: 620px;
    top: 55px;
    width: 400px;
    text-align: center;
    color: var(--navy);
  }
  .contact-label {
    display: block;
    font-size: 50px;
    line-height: 1;
  }
  .contact-phone {
    display: block;
    margin-top: 10px;
    font-size: 66px;
    line-height: 1;
    letter-spacing: -1px;
  }
  .features {
    position: absolute;
    left: 610px;
    top: 228px;
    margin: 0;
    padding: 0;
    list-style: none;
    color: var(--navy);
    font-size: 35px;
    line-height: 44px;
  }
  .features li {
    display: flex;
    align-items: center;
    gap: 10px;
  }
  .features li::before {
    content: "";
    width: 14px;
    height: 14px;
    border-radius: 50%;
    background: linear-gradient(#f6b73c, var(--coral));
  }
  .rule {
    position: absolute;
    left: 4px;
    right: 0;
    top: 399px;
    height: 4px;
    background: var(--amber);
  }
  .web-band {
    position: absolute;
    left: 0;
    right: 0;
    top: 421px;
    bottom: 0;
    background: var(--navy);
    display: flex;
    align-items: center;
    justify-content: center;
  }
  .web-address {
    color: var(--white);
    font-size: 62px;
    letter-spacing: 0.5px;
  }
</style>
</head>
<body>
<div class="canvas">
  <section class="billboard">
    <div class="lake-map" role="img" aria-label="Faint outline map of the lake behind the contact details"></div>

    <div class="brand">
      <span class="brand-mark"></span>
      <h1 class="brand-name">COPPER RIDGE</h1>
      <span class="brand-sub">RESORT &amp; MARINA</span>
    </div>

    <div class="directions">
      <svg width="130" height="78" viewBox="0 0 130 78" aria-hidden="true">
        <polygon points="0,39 75,0 75,20 130,20 130,58 75,58 75,78" fill="#e8553a"/>
      </svg>
      <span class="distance">3 Miles</span>
    </div>

    <div class="contact">
      <span class="contact-label">Call:</span>
      <span class="contact-phone">555-214-0867</span>
    </div>

    <ul class="features">
      <li>Lakefront Cabin Rentals</li>
      <li>Floating Vacation Homes</li>
      <li>New Slips Summer 2022</li>
    </ul>

    <div class="rule"></div>

    <div class="web-band">
      <span class="web-address">www.copperridgeresort.example</span>
    </div>
  </section>
</div>
</body>
</html>
```